Real Estate stationery - need an interesting, eye catching design

I need a letterhead and #10 envelope design in the same theme.
I am looking for an interesting, eye catching design that would stand out in the crowd. I am in the real estate business(which is very competitive) in Florida so standing out and being different is very important to me.
Marguerite(Gwen) Hollowbeck (name), RealtorĀ® (title), 555-555-2863 (cell), sunnygwenhomes@brevomail.com (email), www.sunnygwenhomes.com(website), 915 Pelham Brook Rd.,Ste. 3140, Longwood, FL 32750 (business address)
Industry/Entity Type
Real Estate Agent
Colors
Designer to choose colors to be used in the design.
Look and feel

```html
<!DOCTYPE html>
<html lang="en">
<head>
<meta charset="utf-8">
<title>Homestead Crest Realty – Stationery</title>
<link href="https://fonts.googleapis.com/css2?family=Open+Sans:ital,wght@0,400;0,600;0,700;1,400&display=swap" rel="stylesheet">
<style>
:root{
  --backdrop:#cccccc;
  --paper:#fafafa;
  --brand:#8a6128;
  --ink:#3a3a3a;
  --muted:#6d6d6d;
  --rule:#9a9a9a;
}
*{margin:0;padding:0;box-sizing:border-box}
html,body{width:1200px;height:771px;overflow:hidden}
body{background:var(--backdrop);position:relative;font-family:"Open Sans",sans-serif;color:var(--ink)}

.letterhead{position:absolute;left:115px;top:80px;width:431px;height:610px;background:var(--paper);border-top:4px solid var(--brand)}
.brand-name{display:flex;align-items:center;gap:6px;color:var(--brand);font-weight:600;font-family:"Open Sans",sans-serif;white-space:nowrap}
.brand-name .mark{width:9px;height:9px;background:var(--brand)}
.letterhead .brand-name{position:absolute;left:37px;top:48px;font-size:12px}
.letterhead .divider{position:absolute;left:277px;top:28px;width:1.5px;height:60px;background:var(--rule)}
.contact{position:absolute;left:295px;top:34px}
.contact .name{font-size:9px;font-weight:700;color:#333}
.contact .title{font-size:4.5px;font-style:italic;color:var(--muted);margin-top:1px}
.contact ul{list-style:none;margin-top:9px}
.contact li{display:flex;align-items:center;gap:5px;font-size:6.2px;color:#555;line-height:9.6px}
.contact svg{width:6px;height:6px;fill:var(--brand)}

.letter-body{position:absolute;left:49px;top:143px;width:346px;font-size:6.3px;line-height:11px;color:#5e5e5e;text-align:justify}
.letter-body p{margin-bottom:11px}
.letter-body .salutation{margin-bottom:22px}
.sign-off{position:absolute;left:49px;top:404px;font-size:6.4px;color:#555}
.sign-off .label{font-weight:700;color:#444}
.signature{position:absolute;left:37px;top:424px;width:85px;height:16px;background:linear-gradient(90deg,rgba(74,123,176,.18),rgba(74,123,176,.05))}
.sign-off .role{position:absolute;top:44px;white-space:nowrap}
.letter-footer{position:absolute;left:0;right:0;top:582px;display:flex;justify-content:center;align-items:center;gap:3px;font-size:6.2px;color:#555}
.letter-footer svg{width:6px;height:7px;fill:var(--brand)}

.envelope-front{position:absolute;left:588px;top:170px;width:496px;height:208px;background:var(--paper);border-top:6px solid var(--brand)}
.envelope-front .brand-name{position:absolute;left:22px;top:36px;font-size:11px}
.return-address{position:absolute;left:22px;top:88px;width:102px;text-align:center;font-size:6.2px;line-height:11px;color:#555}

.envelope-back{position:absolute;left:588px;top:392px;width:496px;height:209px;background:var(--paper)}
.envelope-back svg{position:absolute;left:0;top:0}
.flap-url{position:absolute;left:0;right:0;top:28px;text-align:center;font-size:6.4px;color:#f3ead8}
</style>
</head>
<body>

<section class="letterhead" aria-label="Letterhead">
  <div class="brand-name"><span class="mark"></span>Homestead Crest Realty</div>
  <div class="divider"></div>
  <div class="contact">
    <div class="name">Gwen Hollowbeck</div>
    <div class="title">Realtor®</div>
    <ul>
      <li><svg viewBox="0 0 10 10"><path d="M1 3 Q5 0 9 3 L8 4 L6.5 3.5 L6.5 4.5 L8.5 7 L8.5 9 L1.5 9 L1.5 7 L3.5 4.5 L3.5 3.5 L2 4Z"/></svg>555-555-2863</li>
      <li><svg viewBox="0 0 10 10"><rect x="0.5" y="2" width="9" height="6" rx="1"/></svg>sunnygwenhomes@brevomail.com</li>
      <li><svg viewBox="0 0 10 10"><circle cx="5" cy="5" r="4"/></svg>www.sunnygwenhomes.com</li>
    </ul>
  </div>

  <div class="letter-body">
    <p class="salutation">Dear Sir,</p>
    <p>Lorem Ipsum is simply dummy text of the printing and typesetting industry. Lorem Ipsum has been the industry's standard dummy text ever since the 1500s, when an unknown printer took a galley of type and scrambled it to make a type specimen book. It has survived not only five centuries, but also the leap into electronic typesetting, remaining essentially unchanged. It was popularised in the 1960s with the release of Tessamark sheets containing Lorem Ipsum passages, and more recently with desktop publishing software like Quillset Composer including versions of Lorem Ipsum.</p>
    <p>Lorem Ipsum is simply dummy text of the printing and typesetting industry. Lorem Ipsum has been the industry's standard dummy text ever since the 1500s, when an unknown printer took a galley of type and scrambled it to make a type specimen book. It has survived not only five centuries, but also the leap into electronic typesetting, remaining essentially unchanged. It was popularised in the 1960s with the release of Tessamark sheets containing Lorem Ipsum passages, and more recently with desktop publishing software like Quillset Composer including versions of Lorem Ipsum.</p>
    <p>Lorem Ipsum is simply dummy text of the printing and typesetting industry. Lorem Ipsum has been the industry's standard dummy text ever since the 1500s, when an unknown printer took a galley of type and scrambled it to make a type specimen book.</p>
  </div>

  <div class="sign-off">
    <div class="label">Your Name</div>
    <div class="role">CEO &nbsp;|&nbsp; Owner</div>
  </div>
  <div class="signature" role="img" aria-label="Handwritten signature"></div>

  <div class="letter-footer">
    <svg viewBox="0 0 10 12"><path d="M5 0 A4 4 0 0 1 9 4 C9 7 5 12 5 12 C5 12 1 7 1 4 A4 4 0 0 1 5 0Z M5 2.5 A1.5 1.5 0 1 0 5 5.5 A1.5 1.5 0 1 0 5 2.5Z"/></svg>
    915 Pelham Brook Road, Suite 3140, Marrowvale, QN 00750
  </div>
</section>

<section class="envelope-front" aria-label="Envelope front">
  <div class="brand-name"><span class="mark"></span>Homestead Crest Realty</div>
  <div class="return-address">915 Pelham Brook Rd.,<br>Ste. 3140, Marrowvale, QN 00750</div>
</section>

<section class="envelope-back" aria-label="Envelope back">
  <svg width="496" height="66" viewBox="0 0 496 66">
    <path d="M1 0 H495 L482 44 Q476 63 456 64 H40 Q20 63 14 44 Z" fill="var(--brand)"/>
  </svg>
  <div class="flap-url">www.sunnygwenhomes.com</div>
</section>

</body>
</html>
```